Insert sheet for our Dog Food Package

We need an information sheet to go inn our pet food package, with branding, and information on ingredients, nutrition and feeding guidance. We will also need two additional items which will be a variation on the label design:
1) Label for package (detailed label about us and our food)
2) Label for outer shipping box (simple label for branding)
We will start with the information, insert page. The winning designer will then deliver the package and box labels as simplified versions of the same graphical theme.
I have attached samples of an earlier drafts of the insert piece. Please disregard the style, form and colors of the examples given. THEY ARE ONLY THERE TO SHOW WHAT INFORMATION SHOULD BE INCLUDED. All colors and style should be from our logo (attached). All graphics, font styles, and placement of elements need to be YOUR creative design - not a copy of the sample we gave. PLEASE READ THIS AND PLEASE DO NOT SUBMIT ANY VARIATION OF THE EXAMPLES!!!!!!!

Target Market(s)

Pet Owners

Industry/Entity Type

Pet Food

Colors
EB3D1F
EC4F4E
F09395
F8D3D4
FCEDEE

Requirements
Must have
• All new design. New colors (based in the palette of our logo), new graphics, new fonts, new placement of elements.
Should not have
• Please disregard the style, form and colors of the examples given. THEY ARE ONLY THERE TO SHOW WHAT INFORMATION SHOULD BE INCLUDED.

```html
<!DOCTYPE html>
<html lang="en">
<head>
<meta charset="utf-8">
<title>Verano – Dog Food Pouch Label</title>
<link rel="stylesheet" href="https://fonts.googleapis.com/css2?family=Exo+2:wght@400;600;700&family=Kaushan+Script&display=swap">
<style>
  :root {
    --red: #ec4f4e;
    --red-deep: #eb3d1f;
    --line-dark: #9b2326;
    --rose: #f09395;
    --pink: #f8d3d4;
    --blush: #fcedee;
    --white: #ffffff;
    --ink: #2b2b2b;
    --stage: #eef1f4;
    --photo-light: #cfe3a6;
    --photo-mid: #8fbf5a;
    --photo-dark: #4f7f2f;
    --puppy: #f1e3c6;
  }
  * { box-sizing: border-box; margin: 0; padding: 0; }
  html, body { width: 1200px; height: 900px; overflow: hidden; }
  body {
    background: var(--stage);
    font-family: "Exo 2", "Arial Narrow", sans-serif;
    color: var(--ink);
    position: relative;
  }
  .panel {
    position: absolute;
    top: 60px;
    width: 500px;
    height: 780px;
    background: var(--white);
    overflow: hidden;
    box-shadow: 0 6px 24px rgba(0,0,0,.12);
  }
  .panel--back { left: 70px; }
  .panel--front { left: 630px; }
  .panel__shapes { position: absolute; inset: 0; width: 500px; height: 780px; }

  /* Back panel boxes */
  .info-box {
    position: absolute;
    top: 150px;
    width: 200px;
    background: var(--white);
    border: 2px solid var(--pink);
    border-radius: 8px;
    padding: 0 10px 12px;
  }
  .info-box--nutrition { left: 30px; height: 315px; }
  .info-box--feeding { left: 270px; height: 315px; }
  .info-box__title {
    margin: 8px -4px 10px;
    background: var(--red);
    color: var(--white);
    font-weight: 700;
    font-size: 13px;
    line-height: 1.15;
    text-align: center;
    padding: 6px 4px;
    border-radius: 4px;
  }
  .info-box__subtitle {
    font-weight: 700;
    font-size: 11px;
    text-align: center;
    letter-spacing: .3px;
    margin-bottom: 8px;
  }
  .nutrient-list { list-style: none; }
  .nutrient-list li {
    background: var(--pink);
    font-size: 10px;
    font-weight: 600;
    text-align: center;
    padding: 3px 0;
    margin-bottom: 4px;
    border-radius: 3px;
  }
  .ingredients {
    margin-top: 8px;
    font-size: 9.5px;
    line-height: 1.45;
    text-align: center;
  }
  .feeding-table { width: 100%; border-collapse: separate; border-spacing: 3px 5px; }
  .feeding-table th {
    background: var(--rose);
    color: var(--ink);
    font-size: 8.5px;
    font-weight: 700;
    padding: 5px 2px;
  }
  .feeding-table td {
    background: var(--pink);
    font-size: 9.5px;
    text-align: center;
    padding: 5px 2px;
  }

  .brand-tag {
    position: absolute;
    left: 40px;
    top: 665px;
    width: 150px;
    height: 62px;
    background: var(--white);
    border-radius: 8px;
    display: flex;
    align-items: center;
    justify-content: center;
    gap: 8px;
  }
  .brand-tag__dot { width: 22px; height: 22px; border-radius: 50%; background: var(--red); }
  .brand-tag__name { font-weight: 700; font-size: 22px; color: var(--line-dark); letter-spacing: 1px; }
  .promise {
    position: absolute;
    left: 300px;
    top: 650px;
    width: 150px;
    background: var(--white);
    border-radius: 8px;
    padding: 8px;
    font-size: 9px;
    line-height: 1.35;
    text-align: center;
  }

  /* Front panel */
  .badge {
    position: absolute;
    left: 170px;
    top: 20px;
    width: 160px;
    height: 160px;
    border-radius: 50%;
    background: var(--white);
    border: 6px solid var(--pink);
    display: flex;
    flex-direction: column;
    align-items: center;
    justify-content: center;
  }
  .badge__name { font-weight: 700; font-size: 30px; color: var(--line-dark); letter-spacing: 2px; }
  .badge__sub { font-weight: 700; font-size: 10px; color: var(--line-dark); letter-spacing: 2px; text-transform: uppercase; }
  .front__photo { position: absolute; left: 0; top: 0; }
  .front__tagline {
    position: absolute;
    left: 0;
    width: 100%;
    top: 690px;
    text-align: center;
    font-family: "Kaushan Script", cursive;
    font-size: 27px;
    color: var(--white);
  }
</style>
</head>
<body>

<section class="panel panel--back" aria-label="Back of pouch">
  <svg class="panel__shapes" viewBox="0 0 500 780" aria-hidden="true">
    <path d="M0 0H500V118Q250 58 0 118Z" fill="var(--red)"/>
    <path d="M0 128Q250 68 500 128" fill="none" stroke="var(--line-dark)" stroke-width="5"/>
    <path d="M0 630Q250 580 500 630V780H0Z" fill="var(--red)"/>
    <path d="M0 620Q250 570 500 620" fill="none" stroke="var(--line-dark)" stroke-width="5"/>
    <rect x="232" y="0" width="36" height="100" fill="var(--white)"/>
    <rect x="232" y="600" width="36" height="180" fill="var(--white)"/>
  </svg>

  <div class="info-box info-box--nutrition">
    <h2 class="info-box__title">We prepared<br>the best for Shadow</h2>
    <h3 class="info-box__subtitle">NUTRITIONAL INFORMATION</h3>
    <ul class="nutrient-list">
      <li>Protein: 16%</li>
      <li>Total Fat: 9.5%</li>
      <li>Crude Fiber: 2.0%</li>
      <li>Moisture: 72%</li>
    </ul>
    <p class="ingredients">Potassium Citrate, DiCalcium Phosphate, Calcium Carbonate, Garbanzo Beans, Choline Bitartrate, Taurine, Salt, Zinc Proteinate, Magnesium Oxide, Iron Proteinate, Vitamin B-12, Selenium, Niacin, Riboflavin, Calcium Panthothenate, Thiamine, Vitamin A, Vitamin D, Calcium Iodate, Vitamin B6, Folic Acid</p>
  </div>

  <div class="info-box info-box--feeding">
    <h2 class="info-box__title">How much should<br>I feed Shadow?</h2>
    <h3 class="info-box__subtitle">RECOMMENDED FEEDING PLAN</h3>
    <table class="feeding-table">
      <thead><tr><th>APPROXIMATE WEIGHT</th><th>FULL MEAL</th></tr></thead>
      <tbody>
        <tr><td>&lt;20 lbs</td><td>110 g</td></tr>
        <tr><td>20–29 lbs</td><td>200 g</td></tr>
        <tr><td>30–39 lbs</td><td>250 g</td></tr>
        <tr><td>40–54 lbs</td><td>300 g</td></tr>
        <tr><td>55–69 lbs</td><td>350 g</td></tr>
        <tr><td>70–85 lbs</td><td>400 g</td></tr>
        <tr><td>85+ lbs</td><td>500 g</td></tr>
      </tbody>
    </table>
  </div>

  <div class="brand-tag">
    <span class="brand-tag__dot"></span>
    <span class="brand-tag__name">VERANO</span>
  </div>
  <p class="promise">We Revolutionized the industry. Not Formulated to meet a minimum standard, but to develop the maximum health of the whole dog.</p>
</section>

<section class="panel panel--front" aria-label="Front of pouch">
  <svg class="panel__shapes" viewBox="0 0 500 780" aria-hidden="true">
    <path d="M0 0H500V150Q250 90 0 150Z" fill="var(--red)"/>
    <path d="M0 166Q250 106 500 166" fill="none" stroke="var(--line-dark)" stroke-width="6"/>
    <path d="M0 650Q250 600 500 650V780H0Z" fill="var(--red)"/>
    <path d="M0 638Q250 588 500 638" fill="none" stroke="var(--line-dark)" stroke-width="6"/>
  </svg>
  <svg class="front__photo" width="500" height="780" viewBox="0 0 500 780" role="img" aria-label="Photo of a smiling cream Labrador puppy on a leafy green background">
    <defs>
      <radialGradient id="photoTone" cx="50%" cy="55%" r="60%">
        <stop offset="0" stop-color="var(--puppy)"/>
        <stop offset=".45" stop-color="var(--photo-light)"/>
        <stop offset=".8" stop-color="var(--photo-mid)"/>
        <stop offset="1" stop-color="var(--photo-dark)"/>
      </radialGradient>
    </defs>
    <path d="M10 210Q250 150 490 210V600Q250 560 10 600Z" fill="url(#photoTone)"/>
  </svg>
  <div class="badge">
    <span class="badge__name">VERANO</span>
    <span class="badge__sub">The Complete Pup</span>
  </div>
  <p class="front__tagline">Prepared with love for Shadow</p>
</section>

</body>
</html>
```